Harbourline Safety Academy

I'm currently in the process of setting up a First Aid and Lifeguard Training website. The project has already began through a web designer but he is unable to meet the deadline.
There's is already a landing page
http://www.harbourlinesafetyacademy.com.au/
In addition he also started to create the website
https://mockups.quellbrook.example/view/8a41c0d2-55e7-4b19-9c3e-0d7e2a6b91f4-3381/?fullscreen
The home page ideally needs to have a different visual and user journey from the quick landing page created
- The Logo in the top left hand corner looks a bit out of whack, maybe it needs to be bigger ??
-The tabs along the top need to be 'designed' and spaced out equally: home, about, courses, contact, gallery. Can we please remove Accredited First Aid and Lifeguard.
-the blue bar with the tag line needs to be redesigned - that was ok for a landing page but not quite right for actual website, it looks clunky
-all the course info needs to be placed under the courses tab not on the home page. I would like a roll down bar ( Check out Tallowbay Rescue Skills website on their First Aid Course) so the client can book a date and proceed to the checkout basket. I will supply those soon; this will only apply to the Provide First Aid and Provide Cardiopulmonary Resuscitation Courses.
- The rest of the courses can have an enquire option
-the about paragraphs need to go directly under banner
-then a rolling slider with upcoming courses - with each course, rolling to give the home page some pop
- followed by pictures/ images of recent courses linked to gallery page updates or social feed
-remove newsletter
In addition to this I also have a logo designed via pixel bazaar and lots of photos as well as briefs on all the courses that I will offer.
Accredited First Aid and CPR Courses. Lifeguard and Community Safety Programs Programs

```html
<!DOCTYPE html>
<html lang="en">
<head>
<meta charset="utf-8">
<title>Harbourline Safety Academy — First Aid &amp; Lifeguard</title>
<link href="https://fonts.googleapis.com/css2?family=Merriweather:wght@900&family=Montserrat:wght@400;500;600;700&display=swap" rel="stylesheet">
<style>
:root{
  --navy:#0a1935;
  --orange:#f7941d;
  --card:#f9a13b;
  --teal:#2aa3d8;
  --white:#ffffff;
  --ink:#1a1208;
}
*{box-sizing:border-box;margin:0;padding:0}
html,body{width:1200px;height:3513px;overflow:hidden}
body{background:var(--navy);font-family:'Montserrat',sans-serif;color:var(--white);position:relative}
.abs{position:absolute}
.serif{font-family:'Merriweather',serif;font-weight:900}

/* hero */
.hero{left:0;top:0;width:1200px;height:730px;background:linear-gradient(180deg,#3b4147 0%,#3a4a4d 35%,#4b4538 70%,#3d362c 100%);border-bottom:3px solid var(--orange)}
.brand{left:112px;top:94px;display:flex;align-items:center;gap:12px;font-size:19px;font-weight:700;color:var(--orange)}
.brand-dot{width:34px;height:34px;border-radius:50%;background:var(--teal);flex:none}
.nav{top:60px;left:0;width:1200px;height:20px}
.nav a{position:absolute;font-size:11.5px;font-weight:500;color:var(--white);text-decoration:none;letter-spacing:.2px}
.nav a.active{color:var(--orange)}
.nav-underline{left:561px;top:99px;width:48px;height:2px;background:var(--orange)}
.social-top span{position:absolute;top:63px;width:11px;height:11px;border-radius:50%;background:var(--white)}
.hero-title{left:128px;top:270px;font-size:112px;line-height:103px;letter-spacing:1px}
.hero-ornament{left:600px;top:232px;width:190px;height:200px;border-radius:50%;background:radial-gradient(circle,rgba(247,148,29,.55) 0%,rgba(247,148,29,.2) 55%,rgba(247,148,29,0) 72%)}
.hero-lede{left:130px;top:506px;width:600px;font-size:19.5px;line-height:31px}

/* about */
.about-photo{left:110px;top:859px;width:410px;height:410px;border-radius:50%;background:radial-gradient(circle,#6b5a44 0%,#4a5560 60%,#2c6e95 100%);border:6px solid var(--teal)}
.about-title{left:620px;top:890px;font-size:62px}
.about-title em,.testi-title em{font-style:normal;color:var(--orange)}
.about-copy{left:619px;top:995px;width:460px;font-size:16.5px;line-height:31px}
.btn-more{left:620px;top:1223px;width:126px;height:48px;border:2px solid var(--orange);border-radius:24px;display:flex;align-items:center;justify-content:center;font-size:11.5px;font-weight:600}

/* courses */
.courses-band{left:0;top:1411px;width:1200px;height:730px;background:linear-gradient(90deg,#8f8a80 0%,#c4b8a2 40%,#b5ab98 70%,#4f6f7a 100%)}
.course-card{left:140px;top:1561px;width:633px;height:438px;border-radius:40px;background:var(--card)}
.course-title{left:236px;top:1612px;font-size:62px}
.course-sub{left:242px;top:1694px;font-size:19px;font-weight:700;color:var(--ink)}
.course-row{left:244px;display:flex;align-items:center;gap:18px;font-size:16px;color:var(--white)}
.course-row svg{width:20px;height:20px;flex:none}
.course-row b{font-weight:700}
.arrow{width:18px;height:18px}

/* testimonials */
.testi-title{left:0;top:2262px;width:1200px;text-align:center;font-size:64px}
.testi-copy{left:200px;top:2436px;width:800px;text-align:center;font-size:16.5px;line-height:31px}
.testi-name{left:0;top:2594px;width:1200px;text-align:center;font-size:26px;font-weight:600}
.stars{left:555px;top:2649px;display:flex;gap:3px}

/* gallery */
.tile{position:absolute}

/* footer */
.foot-brand{left:120px;top:3322px;width:200px;display:flex;align-items:center;gap:10px;font-size:15px;line-height:20px;font-weight:700;color:var(--orange)}
.foot-head{font-size:20px;font-weight:600}
.foot-links a{position:absolute;left:354px;font-size:12.5px;color:var(--white);text-decoration:none}
.foot-contact{left:544px;display:flex;align-items:center;gap:12px;font-size:12.5px}
.foot-contact svg{width:16px;height:16px;flex:none}
.copy{left:890px;top:3315px;font-size:12px}
.foot-social span{position:absolute;top:3349px;width:28px;height:28px;border-radius:50%;background:var(--white)}
</style>
</head>
<body>

<section class="abs hero" role="img" aria-label="Photo of lifeguard trainees in teal uniforms standing on a beach"></section>
<div class="abs brand"><span class="brand-dot"></span>Harbourline Safety Academy</div>
<nav class="abs nav">
  <a class="active" style="left:566px">HOME</a>
  <a style="left:638px">ABOUT</a>
  <a style="left:716px">COURSES</a>
  <a style="left:809px">GALLERY</a>
  <a style="left:896px">CONTACT</a>
</nav>
<div class="abs nav-underline"></div>
<div class="social-top"><span style="left:1050px"></span><span style="left:1077px"></span><span style="left:1107px"></span></div>
<h1 class="abs hero-title serif">FIRST AID<br>LIFEGUARD</h1>
<div class="abs hero-ornament" role="img" aria-label="Orange hand-lettered ampersand between the headline words"></div>
<p class="abs hero-lede">Harbourline Safety Academy delivers a series of Emergency training accreditation and innovative</p>

<div class="abs about-photo" role="img" aria-label="Circular photo of a CPR training session on the sand"></div>
<h2 class="abs about-title serif">About <em>US</em></h2>
<p class="abs about-copy">Harbourline Safety Academy delivers a series of Emergency training accreditation and innovative general safety awareness programs. From general first aid to Lifeguard training courses, our carefully designed training methods ensure all students leave with clarity and confidence in managing emergency scenarios.</p>
<a class="abs btn-more">VIEW MORE</a>

<section class="abs courses-band" role="img" aria-label="Photo of lifeguards beside a patrol vehicle on the beach"></section>
<div class="abs course-card"></div>
<svg class="abs arrow" style="left:667px;top:1607px" viewBox="0 0 18 18"><path d="M12 2 5 9l7 7" fill="none" stroke="#fff" stroke-width="2"/></svg>
<svg class="abs arrow" style="left:700px;top:1607px" viewBox="0 0 18 18"><path d="M6 2l7 7-7 7" fill="none" stroke="#fff" stroke-width="2"/></svg>
<h2 class="abs course-title serif">Cources</h2>
<div class="abs course-sub">PROVIDE FIRST AID HLTAID011</div>
<div class="abs course-row" style="top:1754px"><svg viewBox="0 0 20 20"><rect x="4" y="1" width="12" height="18" fill="none" stroke="#fff" stroke-width="2"/><circle cx="10" cy="9" r="2.5" fill="#fff"/></svg><span><b>Cost:</b> $150.00</span></div>
<div class="abs course-row" style="top:1795px"><svg viewBox="0 0 20 20"><rect x="1" y="3" width="18" height="16" fill="none" stroke="#fff" stroke-width="2"/><path d="M10 7v5h3" stroke="#fff" stroke-width="2" fill="none"/></svg><span><b>Time:</b> 10.30am-14.30</span></div>
<div class="abs course-row" style="top:1836px"><svg viewBox="0 0 20 20"><path d="M10 19s6-6.5 6-11a6 6 0 0 0-12 0c0 4.5 6 11 6 11z" fill="#fff"/><circle cx="10" cy="8" r="2.3" fill="#f9a13b"/></svg><span><b>Venue:</b> Saltwind Yoga Studio, Bayport</span></div>
<div class="abs course-row" style="top:1877px;left:282px"><b>Reserve your place:</b></div>
<div class="abs course-row" style="top:1918px"><svg viewBox="0 0 20 20"><rect x="1" y="4" width="18" height="12" fill="#fff"/><path d="M1 4l9 7 9-7" fill="none" stroke="#f9a13b" stroke-width="1.5"/></svg><span>callum@harbourlinesafetyacademy.com.au</span></div>

<h2 class="abs testi-title serif">Client <em>Testimonials</em></h2>
<svg class="abs" style="left:572px;top:2368px" width="56" height="42" viewBox="0 0 56 42"><path d="M22 3C8 6 3 18 6 30c2 8 12 10 16 4s0-13-7-12M48 3C34 6 29 18 32 30c2 8 12 10 16 4s0-13-7-12" fill="none" stroke="#fff" stroke-width="2.5"/></svg>
<svg class="abs" style="left:128px;top:2474px" width="16" height="22" viewBox="0 0 16 22"><path d="M13 2 4 11l9 9" fill="none" stroke="#fff" stroke-width="2.5"/></svg>
<svg class="abs" style="left:1054px;top:2474px" width="16" height="22" viewBox="0 0 16 22"><path d="M3 2l9 9-9 9" fill="none" stroke="#fff" stroke-width="2.5"/></svg>
<p class="abs testi-copy">Harbourline Safety Academy delivers a series of Emergency training accreditation and innovative general safety awareness programs. From general first aid to Lifeguard training courses, our carefully designed training methods ensure all students leave with clarity and confidence in managing emergency scenarios.</p>
<div class="abs testi-name">Marcus Ellery</div>
<div class="abs stars">
  <svg width="16" height="15" viewBox="0 0 16 15"><path d="M8 1l2 4.7 5 .4-3.8 3.3 1.2 4.9L8 11.7 3.6 14.3l1.2-4.9L1 6.1l5-.4z" fill="none" stroke="#f7941d"/></svg>
  <svg width="16" height="15" viewBox="0 0 16 15"><path d="M8 1l2 4.7 5 .4-3.8 3.3 1.2 4.9L8 11.7 3.6 14.3l1.2-4.9L1 6.1l5-.4z" fill="none" stroke="#f7941d"/></svg>
  <svg width="16" height="15" viewBox="0 0 16 15"><path d="M8 1l2 4.7 5 .4-3.8 3.3 1.2 4.9L8 11.7 3.6 14.3l1.2-4.9L1 6.1l5-.4z" fill="none" stroke="#f7941d"/></svg>
  <svg width="16" height="15" viewBox="0 0 16 15"><path d="M8 1l2 4.7 5 .4-3.8 3.3 1.2 4.9L8 11.7 3.6 14.3l1.2-4.9L1 6.1l5-.4z" fill="none" stroke="#f7941d"/></svg>
  <svg width="16" height="15" viewBox="0 0 16 15"><path d="M8 1l2 4.7 5 .4-3.8 3.3 1.2 4.9L8 11.7 3.6 14.3l1.2-4.9L1 6.1l5-.4z" fill="none" stroke="#8a93a6"/></svg>
</div>

<div class="tile" style="left:0;top:2778px;width:232px;height:208px;background:linear-gradient(135deg,#9fb4c2,#3a5a6e)" role="img" aria-label="Photo of instructors on the beach with rescue gear"></div>
<div class="tile" style="left:237px;top:2778px;width:257px;height:208px;background:linear-gradient(160deg,#2f5fa8,#1d3f7a)" role="img" aria-label="Photo of a first aid demonstration against a blue wall"></div>
<div class="tile" style="left:0;top:2992px;width:494px;height:206px;background:linear-gradient(180deg,#8fa0ad,#c9c3b8 60%,#3c3a36)" role="img" aria-label="Photo of a lifeguard class group on a boardwalk"></div>
<div class="tile" style="left:499px;top:2778px;width:427px;height:420px;background:linear-gradient(135deg,#c2622a,#6b3b20 60%,#2e8ea8)" role="img" aria-label="Photo of an instructor holding training equipment"></div>
<div class="tile" style="left:931px;top:2778px;width:269px;height:208px;background:linear-gradient(135deg,#d9d6cf,#8a7a66)" role="img" aria-label="Photo of students practising first aid outdoors"></div>
<div class="tile" style="left:931px;top:2992px;width:269px;height:206px;background:linear-gradient(135deg,#3a4552,#2a6fb8 60%,#1c2430)" role="img" aria-label="Photo of a surf instructor beside a vehicle"></div>

<div class="abs foot-brand"><span class="brand-dot" style="width:30px;height:30px"></span><span>Harbourline<br>Safety Academy</span></div>
<div class="abs foot-head" style="left:353px;top:3271px">Useful Links</div>
<div class="foot-links">
  <a style="top:3336px">Home</a><a style="top:3361px">About</a><a style="top:3386px">Courses</a><a style="top:3411px">Gallery</a><a style="top:3436px">Contact</a>
</div>
<div class="abs foot-head" style="left:544px;top:3271px">Contact Us</div>
<div class="abs foot-contact" style="top:3336px"><svg viewBox="0 0 16 16"><path d="M8 15s5-5 5-8.5a5 5 0 0 0-10 0C3 10 8 15 8 15z" fill="none" stroke="#fff" stroke-width="1.3"/><circle cx="8" cy="6.5" r="1.8" fill="none" stroke="#fff"/></svg>Callum Reyes</div>
<div class="abs foot-contact" style="top:3370px"><svg viewBox="0 0 16 16"><path d="M3 1.5l3 .5 1 3-2 1.5c1 2 2.5 3.5 4.5 4.5L11 9l3 1 .5 3c-6 1-13-6-11.5-11.5z" fill="none" stroke="#fff" stroke-width="1.3"/></svg>0400 123 987</div>
<div class="abs foot-contact" style="top:3389px"><svg viewBox="0 0 16 16"><rect x="1" y="3" width="14" height="10" fill="none" stroke="#fff" stroke-width="1.3"/><path d="M1 3l7 6 7-6" fill="none" stroke="#fff" stroke-width="1.3"/></svg><span style="color:var(--orange)">callum@harbourlinesafetyacademy.com.au</span></div>
<div class="abs copy">© 2021 Harbourline Safety Academy</div>
<div class="foot-social"><span style="left:940px"></span><span style="left:981px"></span><span style="left:1022px"></span></div>

</body>
</html>
```